Events Company Needs Website Revamp

Harbor Showcases is an events company that specializes in organizing and marketing large scale consumer and trade events globally.

The new web design should provide easy classification of the events, and allow visitors to find and access the details page within 2 clicks.

There are no strict guidelines on the color theme. It just has to blend naturally with the corporate logo.
Updates

The company logo is uploaded (pdf & ai)

I came across this design which I like very much. Elegant and corporate with nice modern fonttype.

Layout wise, neat and clear. 

Please see how you can emulate the design further. Particularly, highlighting the 2 event arms (Trade/Consumer) clearly.

Target Market(s)

Consumer looking for upcoming events, B2C companies looking to participate, B2B companies looking to connect with other companies

Industry/Entity Type

It Company

Requirements
Must have
• The new design should help to achieve the following objectives:
1) Visitors should be able to easily identify and access the 2 different types of events (i.e. Trade Events and Consumer Events).
2) Visitors should be able to easily find events that interest them (e.g. filter by date, trade or consumer, category [i.e. beauty, retail, F&B, construction, etc.]).
3) Visitors should be able to access an event’s details page within 2 clicks from any page.

Main navigation to include the following links:
- About Us
- Calendar
- Consumer Events
- Trade Events
- Contact Us

Design for Three (3) pages required:
A. Homepage
- Clear differentiation and easy access to the 2 different types of events (trade and consumer)
- Featured area to showcase latest 4-5 events
- Quick way to access events calendar
- Clear call-to-action for newsletter signup
- Social media sharing widgets/buttons
- A section for latest news and press releases
- A section for featured testimonials

B. Events Listing Page
- List of links to all events
- Logos and/or photos of events
- Filter / tags to find events in a specific category (e.g. food, electronics, building & construction, etc.)

C. Events Details Page
- Photo strip to showcase event photos / brochure
- A section with event details (Date, Venue, Event Description, etc.)
- Call-to-action button to visit event website
- Call-to-action button to contact event sales team
- E.g. http://vemlo.com/user/launchgrovehq/launch-weekend-2011 but with the photo strip permanently extended and of a shorter height. Event details and call-to-action buttons should also be easily seen

```html
<!DOCTYPE html>
<html lang="en">
<head>
<meta charset="utf-8">
<title>Harbor Showcases</title>
<link rel="stylesheet" href="https://fonts.googleapis.com/css2?family=Gelasio:ital,wght@0,400;1,400&family=Montserrat:wght@400;500;600;700&display=swap">
<style>
:root{
  --blue:#1f5f96;
  --nav:#1a63a8;
  --orange:#e2661f;
  --red:#d0341d;
  --text:#4a4a4a;
  --line:#d7dde2;
  --testi:#bed3de;
  --news:#f1f2f3;
  --footer:#d3dce2;
  --hero-a:#b7763a;
  --hero-b:#c65a1c;
}
*{margin:0;padding:0;box-sizing:border-box}
html,body{width:1000px;height:1200px;overflow:hidden;background:#fff}
body{position:relative;font-family:"Montserrat",Arial,sans-serif;color:var(--text)}
h1,h2,h3{font-weight:400}
.abs{position:absolute}
.serif{font-family:"Gelasio",Georgia,serif;font-weight:400}
/* header */
.brand-name{left:210px;top:30px;font-size:18px;font-weight:600;color:#333;line-height:1}
.subsidiary{left:221px;top:79px;font-size:6.5px;font-weight:600;color:var(--nav);letter-spacing:.2px}
.call{left:666px;top:19px;color:var(--blue);font-size:11px;font-weight:500}
.phone{left:665px;top:31px;color:var(--red);font-size:18px;font-weight:400;letter-spacing:.3px}
.nav{left:434px;top:78px;width:366px;display:flex;justify-content:space-between;list-style:none}
.nav li{font-size:7.6px;font-weight:600;color:var(--nav);text-transform:uppercase}
.hero{left:206px;top:101px;width:589px;height:288px;background:linear-gradient(180deg,#9a6a3a 0%,var(--hero-a) 45%,var(--hero-b) 100%)}
/* about */
.about-title{left:0;top:400px;width:1000px;text-align:center;font-size:15px;color:var(--blue);letter-spacing:.3px}
.rule{top:410px;height:1px;background:var(--line)}
.about-text{left:212px;top:431px;width:578px;text-align:center;font-size:7.4px;line-height:11.2px;color:var(--text)}
.about-text p+p{margin-top:11px}
.divider{left:190px;top:542px;width:620px;height:14px;background:radial-gradient(ellipse at 50% 0,rgba(170,185,200,.35),rgba(255,255,255,0) 70%)}
/* events */
.card{left:206px;width:406px;height:87px;border:1px solid var(--line)}
.card-photo{left:12px;top:-5px;width:88px;height:88px;border-radius:50%;border:3px solid #fff;box-shadow:0 0 0 1px var(--line)}
.card-title{left:108px;top:-12px;background:#fff;padding:0 5px 0 2px;font-size:16px;color:var(--blue)}
.card-title em,.sec-title em{color:var(--orange)}
.card-text{left:112px;top:13px;width:282px;font-size:7.2px;line-height:11px}
.more{right:9px;bottom:8px;font-size:7.2px;color:#555}
.more::after{content:"";display:inline-block;margin-left:4px;border-left:3px solid #555;border-top:2.5px solid transparent;border-bottom:2.5px solid transparent}
/* calendar */
.cal{left:629px;top:596px;width:166px;height:185px;border:1px solid var(--line);background:#f7f7f7}
.cal-title{left:0;top:-10px;width:164px;text-align:center;line-height:20px}
.cal-title span{background:#fff;padding:0 5px;font-size:16px;color:var(--blue)}
.cal-head{left:6px;top:27px;width:153px;height:22px;background:var(--red);border-radius:3px 3px 0 0;color:#fff;font-size:8.5px;font-weight:500;text-align:center;line-height:22px;letter-spacing:.5px}
.cal-head svg{position:absolute;top:7px}
.cal-grid{left:6px;top:49px;width:153px;border-collapse:collapse;background:#fff}
.cal-grid th{height:16px;font-size:6px;font-weight:500;color:#999;background:#f4f4f4}
.cal-grid td{width:22px;height:21.5px;border:1px solid #e3e3e3;text-align:center;font-size:10px;color:#333}
.cal-grid td.sel{background:var(--red);color:#fff}
.cal-grid td.mark{background:#ddd;color:#666}
/* lower */
.sec-title{font-size:16px;color:var(--blue)}
.testi{left:206px;top:926px;width:289px;height:102px;background:var(--testi)}
.testi-photo{left:13px;top:13px;width:58px;height:58px;border:3px solid #fff;background:linear-gradient(135deg,#d9c6b0,#9bb0c2)}
.testi-text{left:84px;top:11px;width:195px;font-size:7.2px;line-height:11px;color:#fff}
.dots{left:465px;top:912px;display:flex;gap:5px}
.dots i{width:4px;height:4px;border-radius:50%;background:#c7d4dd}
.dots i:first-child{background:#9fb8c8}
.author{left:398px;top:1033px;font-size:8px;font-style:italic;color:#444}
.news{left:506px;top:926px;width:289px;height:102px;background:var(--news)}
.news-item{left:13px;display:flex;gap:11px}
.news-photo{width:31px;height:31px;background:linear-gradient(135deg,#e4d4c2,#aab7c2)}
.news-date{font-size:6.5px;color:#777}
.news-text{font-size:7.2px;line-height:11px;color:#444;width:225px}
/* footer */
.footer{left:108px;top:1068px;width:784px;height:132px;background:var(--footer);border-top:4px solid #c4d0d8}
.signup{left:104px;top:14px;width:182px;height:86px;background:var(--orange);color:#fff;padding:5px 10px}
.signup h3{font-size:15px;font-weight:500;letter-spacing:.5px}
.signup p{font-size:7.2px;line-height:10px;margin-top:2px}
.signup-field{position:absolute;left:8px;top:52px;width:130px;height:17px;background:#fff;font-size:7px;color:#888;padding:4px 6px}
.signup-btn{position:absolute;left:138px;top:52px;width:42px;height:17px;background:var(--blue);font-size:7.5px;font-weight:600;text-align:center;line-height:17px}
.fhead{font-size:7.2px;font-weight:700;color:var(--blue);text-transform:uppercase}
.social{left:305px;top:35px;display:flex;gap:5px}
.social i{width:21px;height:21px;border-radius:3px;background:#3e7fb5}
.flist{list-style:none;font-size:6.8px;line-height:12.4px;color:#444;margin-top:6px}
.copy{left:90px;top:110px;width:602px;border-top:1px solid #bfcad2;padding-top:4px;text-align:right;font-size:6.8px;color:#333}
</style>
</head>
<body>

<header>
  <div class="abs brand-name">Harbor Showcases</div>
  <div class="abs subsidiary">A SUBSIDIARY OF KPL</div>
  <div class="abs call">CALL NOW!</div>
  <div class="abs phone">555 0142 7788</div>
  <ul class="abs nav">
    <li>Home</li><li>About Us</li><li>Calendar</li><li>Consumer Events</li><li>Trade Events</li><li>Contact Us</li>
  </ul>
</header>

<div class="abs hero" role="img" aria-label="Photo of a smiling business team in suits standing in a conference hall"></div>

<section>
  <div class="abs rule" style="left:240px;width:132px"></div>
  <div class="abs rule" style="left:628px;width:132px"></div>
  <h1 class="abs about-title serif">ABOUT HARBOR SHOWCASES</h1>
  <div class="abs about-text">
    <p>Lorem Ipsum is simply dummy text of the printing and typesetting industry. Lorem Ipsum has been the industry's standard dummy text ever since the 1500s, when an unknown printer took a galley of type and scrambled it to make a type specimen book. It has survived not only five centuries, but also the leap into electronic typesetting, remaining essentially unchanged. It was popularised in the 1960s with the release of Typeset sheets containing Lorem Ipsum passages, and more recently with desktop publishing software like Orbit PageSetter including versions of Lorem Ipsum.</p>
    <p>Contrary to popular belief, Lorem Ipsum is not simply random text. It has roots in a piece of classical Latin literature from 45 BC, making it over 2000 years old. Ronald Marsh, a Latin professor at Hillcrest College in Virginia, looked up one of the more obscure Latin words, consectetur, from a Lorem Ipsum passage, and going through the cites of the word in classical literature, discovered the undoubtable source.</p>
  </div>
  <div class="abs divider"></div>
</section>

<section>
  <article class="abs card" style="top:592px">
    <div class="abs card-photo" role="img" aria-label="Photo of trade event attendees in a meeting" style="background:linear-gradient(135deg,#e6c9a8,#9fb3c6)"></div>
    <h2 class="abs card-title serif">Trade <em>Events</em></h2>
    <p class="abs card-text">Lorem Ipsum is simply dummy text of the printing and typesetting industry. Lorem Ipsum has been the industry's standard dummy text ever since the 1500s, when an unknown printer took a galley of type and scrambled it to make a type specimen booktially unchanged.</p>
    <span class="abs more">Read More</span>
  </article>
  <article class="abs card" style="top:696px">
    <div class="abs card-photo" role="img" aria-label="Photo of an audience at a consumer event" style="background:linear-gradient(135deg,#4a5a6a,#b39a82)"></div>
    <h2 class="abs card-title serif">Consumer <em>Events</em></h2>
    <p class="abs card-text">Lorem Ipsum is simply dummy text of the printing and typesetting industry. Lorem Ipsum has been the industry's standard dummy text ever since the 1500s, when an unknown printer took a galley of type and scrambled it to make a type specimen booktially unchanged.</p>
    <span class="abs more">Read More</span>
  </article>
  <article class="abs card" style="top:800px">
    <div class="abs card-photo" role="img" aria-label="Photo of a business conference team" style="background:linear-gradient(135deg,#d9485a,#8c939c)"></div>
    <h2 class="abs card-title serif">Conferences <em>Events</em></h2>
    <p class="abs card-text">Lorem Ipsum is simply dummy text of the printing and typesetting industry. Lorem Ipsum has been the industry's standard dummy text ever since the 1500s, when an unknown printer took a galley of type and scrambled it to make a type specimen booktially unchanged.</p>
    <span class="abs more">Read More</span>
  </article>

  <aside class="abs cal">
    <h2 class="abs cal-title serif"><span>Calendar</span></h2>
    <div class="abs cal-head">
      <svg style="left:6px" width="6" height="8" viewBox="0 0 6 8"><path d="M5 1 2 4l3 3" stroke="#fff" stroke-width="1.6" fill="none"/></svg>
      MAY 2012
      <svg style="right:6px" width="6" height="8" viewBox="0 0 6 8"><path d="M1 1l3 3-3 3" stroke="#fff" stroke-width="1.6" fill="none"/></svg>
    </div>
    <table class="abs cal-grid">
      <tr><th>SUN</th><th>MON</th><th>TUE</th><th>WED</th><th>THU</th><th>FRI</th><th>SAT</th></tr>
      <tr><td></td><td>1</td><td>2</td><td>3</td><td>4</td><td>5</td><td>6</td></tr>
      <tr><td>7</td><td>8</td><td>9</td><td>10</td><td>11</td><td class="mark">12</td><td>13</td></tr>
      <tr><td>14</td><td>15</td><td class="sel">16</td><td>17</td><td>18</td><td>19</td><td>20</td></tr>
      <tr><td>21</td><td>22</td><td>23</td><td>24</td><td>25</td><td>26</td><td>27</td></tr>
      <tr><td>28</td><td>29</td><td>30</td><td>31</td><td></td><td></td><td></td></tr>
    </table>
  </aside>
</section>

<section>
  <h2 class="abs sec-title serif" style="left:206px;top:904px">Client <em>Testimonials</em></h2>
  <div class="abs dots"><i></i><i></i><i></i></div>
  <div class="abs testi">
    <div class="abs testi-photo" role="img" aria-label="Photo of a client team"></div>
    <p class="abs testi-text">Lorem Ipsum is simply dummy text of the printing and typesetting industry. Lorem Ipsum has been the industry's standard dummy text 1500s, when an unknown printer took a galley of type and crambled it to make a .booktially unchanged.</p>
  </div>
  <svg class="abs" style="left:379px;top:1027px" width="12" height="17" viewBox="0 0 12 17"><path d="M0 0h12L7 17z" fill="#bed3de"/></svg>
  <span class="abs author">Jana Smyth</span>

  <h2 class="abs sec-title serif" style="left:507px;top:904px">Latest News &amp; <em>Press Releases</em></h2>
  <div class="abs news">
    <div class="abs news-item" style="top:11px">
      <div class="news-photo" role="img" aria-label="News thumbnail photo"></div>
      <div><div class="news-date">16 March, 2012</div><p class="news-text">Lorem Ipsum is simply dummy text of the printing and type setting industry...</p></div>
    </div>
    <div class="abs news-item" style="top:54px">
      <div class="news-photo" role="img" aria-label="News thumbnail photo"></div>
      <div><div class="news-date">28 April, 2012</div><p class="news-text">Lorem Ipsum is simply dummy text of the printing and type setting industry...</p></div>
    </div>
    <span class="abs more" style="right:13px;bottom:5px">More News</span>
  </div>
</section>

<footer class="abs footer">
  <div class="abs signup">
    <h3>NEWSLETTER</h3>
    <p>Lorem Ipsum is simply dummy text of the printing and typesetting industry.</p>
    <div class="signup-field">enter your e-mail address</div>
    <div class="signup-btn">SUBMIT</div>
  </div>
  <div class="abs fhead" style="left:304px;top:17px">Connect with us</div>
  <div class="abs social" aria-label="Social media links"><i></i><i></i><i></i><i></i></div>
  <div class="abs" style="left:442px;top:17px"><div class="fhead">Quick Links</div>
    <ul class="flist"><li>Home</li><li>About us</li><li>Calendar</li><li>Trade Events</li><li>Consumer Events</li></ul></div>
  <div class="abs" style="left:520px;top:17px"><div class="fhead">Events</div>
    <ul class="flist"><li>Popular Events</li><li>Culture Events</li><li>Musical Events</li><li>Fashion Events</li><li>Corporate Events</li></ul></div>
  <div class="abs" style="left:593px;top:17px"><div class="fhead">Contact Us</div>
    <p class="flist" style="width:80px">Lorem Ipsum is simply dummy text of the printing and type setting industry.</p></div>
  <div class="abs copy">Copyright© 2012 Harbor. All Right Reserved.</div>
</footer>

</body>
</html>
```